Tidal Pines - explore habits of productive people

Tidal Pines is a social place around habits and productivity

The full brief below:

https://docs.quorvane.net/document/d/7Rt-PWMZXK4ubEhqNcs-V2Ytm9Gx8KdfHzJqBsQwnyrT/edit?usp=sharing

Colors

Designer to choose colors to be used in the design.

Requirements
Must have
• - a feed page to display habits
• - a habit page to add a habit
• / clean, no cluttered design, lots of white space
• / inspired by lattice design or other design system
Nice to have
• - user page

```html
<!DOCTYPE html>
<html lang="en">
<head>
<meta charset="utf-8">
<title>Tidal Pines – Feed</title>
<link href="https://fonts.googleapis.com/css2?family=Raleway:wght@400;500;600;700&display=swap" rel="stylesheet">
<style>
:root{
  --blue:#169be8;
  --blue-active:#138ae2;
  --blue-line:#3aaaed;
  --orange:#f7a21b;
  --page:#dcdcdc;
  --white:#ffffff;
  --ink:#2a2a2a;
  --muted:#9a9a9a;
  --rule:#d4d4d4;
  --avatar:#b89a84;
}
*{box-sizing:border-box;margin:0;padding:0}
html,body{width:1200px;height:1063px;overflow:hidden;background:var(--white);font-family:'Raleway',sans-serif;color:var(--ink)}
.app{position:relative;width:1200px;height:1063px}
.topbar{position:absolute;left:0;top:0;width:1200px;height:102px;background:var(--white)}
.brand{position:absolute;left:42px;top:30px;font-size:33px;font-weight:700;color:var(--blue);letter-spacing:-.3px}
.user{position:absolute;right:0;top:0;height:102px}
.user-name{position:absolute;right:152px;top:34px;font-size:17px;font-weight:700;color:var(--blue);white-space:nowrap}
.user-logout{position:absolute;right:152px;top:59px;font-size:12px;font-weight:700;color:var(--orange)}
.user-avatar{position:absolute;right:82px;top:24px;width:57px;height:57px;border-radius:50%;background:linear-gradient(160deg,#d9cfc7,#a88a76)}
.add-btn{position:absolute;right:35px;top:35px;width:36px;height:36px;border-radius:50%;background:var(--orange)}
.sidebar{position:absolute;left:0;top:102px;width:258px;height:899px;background:var(--blue)}
.nav-item{display:flex;align-items:center;height:63.5px;border-bottom:1px solid var(--blue-line);color:var(--white);font-size:19px;font-weight:700}
.nav-item.is-active{background:var(--blue-active);border-bottom:none;height:58px}
.nav-item svg{width:34px;height:34px;margin:0 20px 0 52px;flex:none}
.main{position:absolute;left:258px;top:102px;width:942px;height:899px;background:var(--page)}
.page-title{position:absolute;left:41px;top:29px;font-size:29px;font-weight:400;color:#333}
.post{position:absolute;left:40px;width:838px;height:204px;background:var(--white);border-radius:3px;box-shadow:0 2px 4px rgba(0,0,0,.14)}
.post-head{position:absolute;left:29px;top:21px;display:flex;align-items:center}
.post-avatar{width:48px;height:48px;border-radius:50%;background:linear-gradient(160deg,#cdb7a4,#7c5f4c)}
.post-author{margin-left:11px}
.post-author strong{display:block;font-size:19px;font-weight:600;line-height:1.1}
.post-author span{display:block;font-size:13.5px;font-weight:600;color:#555}
.post-text{position:absolute;left:38px;top:88px;font-size:19px;font-weight:400}
.post-comment{position:absolute;left:0;bottom:0;width:100%;height:50px;border-top:1px solid var(--rule);display:flex;align-items:center;justify-content:space-between;padding:0 18px 0 33px;font-size:16px;color:var(--muted)}
.load-more{position:absolute;left:432px;top:803px}
.footer{position:absolute;left:0;top:1001px;width:1200px;height:62px;background:var(--white);text-align:center;padding-top:22px;font-size:13.5px;color:#555}
</style>
</head>
<body>
<div class="app">
  <header class="topbar">
    <div class="brand">Tidal Pines</div>
    <div class="user">
      <div class="user-name">Evan Carlisle</div>
      <div class="user-logout">Logout</div>
      <div class="user-avatar" role="img" aria-label="Profile photo of the signed-in user"></div>
      <div class="add-btn"><svg width="36" height="36" viewBox="0 0 36 36"><path d="M18 10v16M10 18h16" stroke="#fff" stroke-width="3" stroke-linecap="round"/></svg></div>
    </div>
  </header>

  <nav class="sidebar">
    <div class="nav-item is-active"><svg viewBox="0 0 34 34" fill="none" stroke="#fff" stroke-width="1.4"><rect x="2" y="2" width="24" height="30"/><path d="M26 10h6v20a2 2 0 0 1-4 0V10M6 7h16v6H6zM6 17h16M6 21h16M6 25h16"/></svg>Feed</div>
    <div class="nav-item"><svg viewBox="0 0 34 34" fill="none" stroke="#fff" stroke-width="1.4"><circle cx="7" cy="6" r="3"/><circle cx="17" cy="5" r="3"/><circle cx="27" cy="6" r="3"/><path d="M2 32V15q5-4 10 0v17M12 32V13q5-4 10 0v19M22 32V15q5-4 10 0v17"/></svg>Groups</div>
    <div class="nav-item"><svg viewBox="0 0 34 34" fill="none" stroke="#fff" stroke-width="1.4"><rect x="2" y="7" width="30" height="20"/><path d="M2 7l15 12L32 7M2 27l11-10M32 27L21 17"/></svg>Message</div>
    <div class="nav-item"><svg viewBox="0 0 34 34" fill="none" stroke="#fff" stroke-width="1.4"><path d="M8 2h14l6 6v24H8zM22 2v6h6M5 5v30h20M12 13h12M12 17h12M12 21h12M12 25h12"/></svg>Document</div>
    <div class="nav-item"><svg viewBox="0 0 34 34" fill="none" stroke="#fff" stroke-width="1.4"><rect x="2" y="14" width="6" height="18"/><rect x="13" y="3" width="6" height="29"/><rect x="24" y="20" width="6" height="12"/></svg>Polls</div>
    <div class="nav-item"><svg viewBox="0 0 34 34" fill="none" stroke="#fff" stroke-width="1.4"><path d="M9 3h16v9a8 8 0 0 1-16 0zM9 6H3q0 8 7 9M25 6h6q0 8-7 9M17 20v6M11 26h12v5H11z"/></svg>Quiz</div>
    <div class="nav-item"><svg viewBox="0 0 34 34" fill="none" stroke="#fff" stroke-width="1.4"><path d="M5 5h24v27H5zM11 2v6M23 2v6"/><circle cx="17" cy="18" r="7"/><path d="M14 21l3-7 3 7M15 19h4"/></svg>Grades</div>
  </nav>

  <main class="main">
    <h1 class="page-title">Feeds</h1>

    <article class="post" style="top:85px">
      <div class="post-head"><div class="post-avatar" role="img" aria-label="Author photo"></div><div class="post-author"><strong>Author Name</strong><span>10 mins ago</span></div></div>
      <p class="post-text">After I pour my morning cup of coffee, I will meditate for sixty seconds.</p>
      <div class="post-comment">Add a Comment<svg width="22" height="18" viewBox="0 0 22 18"><path d="M13 1l8 7-8 7v-4C7 11 3 13 1 17c0-7 4-11 12-11z" fill="#bdbdbd"/></svg></div>
    </article>

    <article class="post" style="top:330px;left:42px">
      <div class="post-head"><div class="post-avatar" role="img" aria-label="Author photo"></div><div class="post-author"><strong>Author Name</strong><span>10 mins ago</span></div></div>
      <p class="post-text">After I meditate for sixty seconds, I will write my to-do list for the day</p>
      <div class="post-comment">Add a Comment<svg width="22" height="18" viewBox="0 0 22 18"><path d="M13 1l8 7-8 7v-4C7 11 3 13 1 17c0-7 4-11 12-11z" fill="#bdbdbd"/></svg></div>
    </article>

    <article class="post" style="top:568px;left:41px">
      <div class="post-head"><div class="post-avatar" role="img" aria-label="Author photo"></div><div class="post-author"><strong>Author Name</strong><span>10 mins ago</span></div></div>
      <p class="post-text">After I write my to-do list for the day, I will immediately begin my first task</p>
      <div class="post-comment">Add a Comment<svg width="22" height="18" viewBox="0 0 22 18"><path d="M13 1l8 7-8 7v-4C7 11 3 13 1 17c0-7 4-11 12-11z" fill="#bdbdbd"/></svg></div>
    </article>

    <svg class="load-more" width="22" height="30" viewBox="0 0 22 30" fill="none" stroke="#444" stroke-width="1.6"><path d="M11 1v27M2 19l9 9 9-9"/></svg>
  </main>

  <footer class="footer">© 2018 Company Name&nbsp; All right reserved&nbsp; Term of Use</footer>
</div>
</body>
</html>
```